Artist needs a business card for her pencil portraits and streetscapes

My mum is an artist and does fabulous portraits and sketches with pencil and needs a business card.
She likes designs that are a bit weird or unusual. The winning design will NOT be a slick modern corporate looking logo. It should be a little bit rustic and different. Interesting patterns and textures would be great, it doesn't even need to look like a business card! Come up with something unique!

Target Market(s)

Older clientele looking for family portraits

Industry/Entity Type

Artists

Contact Information for Business Card

Basically just need the name and contact details

Font styles to use
Decorative
Script

Requirements
Must have
• Lena Brodsworth
• Artist
• 0427913562
• lenabrodsworth@quillpost.example
Nice to have
• Weird artistic backgrounds, interesting textures, unusual designs for an artistic woman.
Should not have
• Nothing ultra modern and nothing corporate looking.

```html
<!DOCTYPE html>
<html lang="en">
<head>
<meta charset="utf-8">
<title>Lena Brodsworth — Artist Business Card</title>
<link rel="stylesheet" href="https://fonts.googleapis.com/css2?family=Caveat:wght@500;600&display=swap">
<style>
  :root {
    --backdrop: #e8e2d7;
    --paper-light: #efe2c2;
    --paper-mid: #e4cfa1;
    --paper-stain: #c98a3e;
    --paper-edge: #b8752f;
    --ink: #4a2812;
    --ink-highlight: rgba(255, 244, 220, 0.55);
  }

  html, body {
    margin: 0;
    width: 1200px;
    height: 1200px;
    overflow: hidden;
    background: var(--backdrop);
  }

  .canvas {
    width: 1200px;
    height: 1200px;
    display: flex;
    align-items: center;
    justify-content: center;
  }

  .business-card {
    position: relative;
    width: 1000px;
    height: 620px;
    background:
      radial-gradient(ellipse 22% 55% at 0% 78%, rgba(201, 138, 62, 0.75), rgba(201, 138, 62, 0) 70%),
      radial-gradient(ellipse 18% 30% at 4% 20%, rgba(201, 138, 62, 0.35), rgba(201, 138, 62, 0) 70%),
      radial-gradient(ellipse 30% 20% at 30% 4%, rgba(201, 138, 62, 0.3), rgba(201, 138, 62, 0) 70%),
      radial-gradient(ellipse 20% 40% at 100% 60%, rgba(201, 138, 62, 0.28), rgba(201, 138, 62, 0) 70%),
      radial-gradient(ellipse 25% 18% at 60% 100%, rgba(201, 138, 62, 0.22), rgba(201, 138, 62, 0) 70%),
      radial-gradient(ellipse 60% 55% at 55% 48%, var(--paper-light), var(--paper-mid) 100%);
    box-shadow: inset 0 0 40px rgba(184, 117, 47, 0.25);
    color: var(--ink);
    font-family: "Caveat", cursive;
  }

  .card-content {
    position: absolute;
    inset: 0;
    text-align: center;
  }

  .card-name {
    position: absolute;
    left: 0;
    right: 0;
    top: 160px;
    margin: 0;
    font-size: 96px;
    font-weight: 500;
    line-height: 1;
    letter-spacing: 1px;
    text-shadow: 0 1px 0 var(--ink-highlight);
  }

  .card-title {
    position: absolute;
    left: 0;
    right: 0;
    top: 262px;
    margin: 0;
    font-size: 64px;
    font-weight: 500;
    line-height: 1;
    text-shadow: 0 1px 0 var(--ink-highlight);
  }

  .contact-line {
    position: absolute;
    left: 0;
    right: 0;
    display: flex;
    align-items: center;
    justify-content: center;
    gap: 14px;
    margin: 0;
    font-size: 46px;
    font-weight: 500;
    line-height: 1;
    letter-spacing: 1px;
    text-shadow: 0 1px 0 var(--ink-highlight);
  }

  .contact-phone { top: 368px; }
  .contact-email { top: 430px; }

  .contact-icon {
    width: 30px;
    height: 24px;
    fill: var(--ink);
    flex: none;
  }
</style>
</head>
<body>
  <main class="canvas">
    <section class="business-card" aria-label="Business card">
      <div class="card-content">
        <h1 class="card-name">Lena Brodsworth</h1>
        <p class="card-title">Artist</p>
        <p class="contact-line contact-phone">
          <svg class="contact-icon" viewBox="0 0 30 24" aria-hidden="true">
            <path d="M2 8 C2 3 28 3 28 8 L28 10 L21 10 L21 7 C18 6 12 6 9 7 L9 10 L2 10 Z"/>
            <path d="M7 11 L23 11 L27 21 L3 21 Z"/>
            <circle cx="15" cy="16" r="3" fill="var(--paper-light)"/>
          </svg>
          <span>0427913562</span>
        </p>
        <p class="contact-line contact-email">
          <svg class="contact-icon" viewBox="0 0 30 24" aria-hidden="true">
            <rect x="2" y="4" width="26" height="17"/>
            <path d="M3 5 L15 14 L27 5" fill="none" stroke="var(--paper-light)" stroke-width="2"/>
          </svg>
          <span>lenabrodsworth@quillpost.example</span>
        </p>
      </div>
    </section>
  </main>
</body>
</html>
```